Update a high tech public relations agency website

Hi! I am looking for a nice, clean refresh of my website. The URL is: www.bluemarkcomms.example.

Here's what I'm hoping for:
*To be able to go in to the Wordpress site and change text by myself once the design is set.
*To be able to go in and create a blog.

Here are examples of designs that I like. I'd like to see something along these lines:
www.pindlequill.example
www.GiveOver.example
www.ByCrew.example
www.Steadymailer.example
www.PostGlean.example

Some other things to note that may help:
*No white text with black background.
*I'm open to different color schemes. I like blue, green and red.
Updates

Hi all, Thanks for your interest in this project. Couple of things to note: please use the subheads in blue for the text. I don't want to use inbound marketing as the lead in. The up front text should be High Tech and AdTech Public Relations. Results Driven Media Relations. Content Strategy. Also, please....no stock images of people smiling or shaking hands or doing other fake corporate activities. Graphics would be nice. Thank you.

Industry/Entity Type

Tech

```html
<!DOCTYPE html>
<html lang="en">
<head>
<meta charset="utf-8">
<title>Bluemark Communications</title>
<link rel="stylesheet" href="https://fonts.googleapis.com/css2?family=Gelasio:wght@400&family=Open+Sans:wght@400;600&display=swap">
<style>
  :root {
    --brand-blue: #1a4d7c;
    --nav-blue: #245c8e;
    --accent-red: #f42a28;
    --ink: #1e1e1e;
    --body-ink: #333333;
    --panel-light: #f7f7f7;
    --panel-mid: #ececec;
    --white: #ffffff;
  }
  * { margin: 0; padding: 0; box-sizing: border-box; }
  html, body { width: 1042px; height: 1200px; overflow: hidden; background: var(--white); }
  body { font-family: "Open Sans", sans-serif; color: var(--ink); }
  .page { position: relative; width: 1042px; height: 1200px; overflow: hidden; }

  /* Header */
  .site-header {
    position: absolute; left: 0; top: 0; width: 1042px; height: 96px;
    background: linear-gradient(180deg, #f4f4f4, #ececec);
    border-bottom: 1px solid #dedede;
  }
  .brand { position: absolute; left: 34px; top: 24px; line-height: 1; }
  .brand-name { display: block; font-family: "Gelasio", serif; font-size: 34px; color: var(--brand-blue); letter-spacing: -0.5px; }
  .brand-sub { display: block; font-family: "Gelasio", serif; font-size: 15px; color: var(--brand-blue); letter-spacing: 0.6px; margin-top: 1px; }
  .main-nav { position: absolute; left: 265px; top: 37px; display: flex; gap: 18px; }
  .main-nav a { font-size: 15px; color: var(--nav-blue); text-decoration: none; padding-bottom: 3px; }
  .main-nav a.is-active { border-bottom: 3px solid var(--brand-blue); }
  .social { position: absolute; left: 927px; top: 34px; display: flex; gap: 1px; }
  .social span { width: 25px; height: 25px; display: block; }
  .social .s1 { background: #1da1e6; }
  .social .s2 { background: #2d4f96; }
  .social .s3 { background: #c9c9c9; display: flex; align-items: center; justify-content: center; }

  /* Title */
  .page-title {
    position: absolute; left: 0; top: 118px; width: 1042px; text-align: center;
    font-family: "Gelasio", serif; font-size: 29px; font-weight: 400; color: var(--ink);
    white-space: nowrap;
  }

  /* Hero */
  .side-panel {
    position: absolute; left: 0; top: 181px; width: 262px; height: 518px;
    background: radial-gradient(ellipse at 80% 40%, #ffffff 0%, var(--panel-light) 50%, var(--panel-mid) 100%);
  }
  .service-list { list-style: none; position: absolute; left: 0; top: 22px; width: 262px; }
  .service-list li { height: 35px; line-height: 34px; padding-left: 34px; font-size: 14.5px; color: var(--ink); }
  .service-list li.is-active { background: var(--accent-red); color: var(--white); }
  .cta-button {
    position: absolute; left: 33px; top: 289px; height: 40px; width: 168px;
    background: var(--brand-blue); color: var(--white); font-size: 17px; line-height: 40px; padding-left: 22px;
    clip-path: polygon(0 0, 86% 0, 100% 50%, 86% 100%, 0 100%);
  }
  .phone-icon { position: absolute; left: 107px; top: 358px; }
  .phone-number { position: absolute; left: 34px; top: 390px; font-size: 27px; color: var(--brand-blue); letter-spacing: -0.3px; }

  .tile { position: absolute; width: 255px; height: 256px; }
  .tile-intro { left: 262px; top: 181px; background: var(--accent-red); color: var(--white); }
  .tile-intro p { position: absolute; left: 24px; top: 58px; width: 228px; font-size: 18px; line-height: 23px; letter-spacing: -0.5px; }
  .arrow-button {
    position: absolute; left: 26px; top: 146px; width: 152px; height: 40px;
    background: var(--white); color: var(--accent-red); font-size: 17px; line-height: 40px; padding-left: 21px;
    clip-path: polygon(0 0, 84% 0, 100% 50%, 84% 100%, 0 100%);
  }
  .photo.p1 { left: 524px; top: 181px; background: linear-gradient(160deg, #d9d2cc, #8a8580 50%, #3b3f46); }
  .photo.p2 { left: 787px; top: 181px; width: 255px; background: linear-gradient(110deg, #f3ece6, #e4d6cc 60%, #3a3c40); }
  .photo.p3 { left: 262px; top: 443px; background: linear-gradient(160deg, #2e3238, #5c5e62 55%, #e8e8e8); }
  .photo.p4 { left: 524px; top: 443px; background: linear-gradient(170deg, #55585d, #a4a4a6 45%, #f2f2f2); }
  .photo.p5 { left: 787px; top: 443px; width: 255px; background: linear-gradient(200deg, #2f3134, #b9b9b9 45%, #f4f4f4); }

  /* About */
  .about-heading { position: absolute; left: 33px; top: 774px; font-family: "Gelasio", serif; font-size: 41px; font-weight: 400; color: var(--brand-blue); letter-spacing: -0.8px; }
  .small-arrow {
    position: absolute; left: 33px; top: 830px; width: 85px; height: 21px;
    background: var(--accent-red); color: var(--white); font-size: 10px; line-height: 21px; padding-left: 12px;
    clip-path: polygon(0 0, 84% 0, 100% 50%, 84% 100%, 0 100%);
  }
  .feature-card {
    position: absolute; top: 767px; height: 321px; width: 255px;
    border-top: 6px solid var(--brand-blue);
    background: radial-gradient(ellipse at 60% 55%, #ffffff 0%, #f6f6f6 55%, #eaeaea 100%);
    padding: 42px 22px 0 32px;
  }
  .feature-card.c1 { left: 262px; }
  .feature-card.c2 { left: 524px; }
  .feature-card.c3 { left: 787px; }
  .feature-card h3 { font-family: "Gelasio", serif; font-weight: 400; font-size: 15px; line-height: 17.5px; color: var(--ink); margin-bottom: 16px; white-space: nowrap; }
  .feature-card p { font-size: 10.4px; line-height: 14.5px; color: var(--body-ink); margin-bottom: 14.5px; }

  /* Footer */
  .site-footer { position: absolute; left: 0; top: 1145px; width: 1042px; height: 55px; background: var(--brand-blue); color: var(--white); }
  .footer-links { position: absolute; left: 24px; top: 15px; font-size: 9.8px; }
</style>
</head>
<body>
<div class="page">
  <header class="site-header">
    <div class="brand">
      <span class="brand-name">Bluemark</span>
      <span class="brand-sub">COMMUNICATIONS</span>
    </div>
    <nav class="main-nav">
      <a href="#">Home</a>
      <a href="#" class="is-active">About Us</a>
      <a href="#">What we do</a>
      <a href="#">Principal</a>
      <a href="#">Services</a>
      <a href="#">Contact</a>
    </nav>
    <div class="social" aria-label="Social links">
      <span class="s1"></span>
      <span class="s2"></span>
      <span class="s3">
        <svg width="15" height="11" viewBox="0 0 15 11"><rect x="0.5" y="0.5" width="14" height="10" fill="none" stroke="#fff"/><path d="M0.5 0.5 L7.5 6 L14.5 0.5" fill="none" stroke="#fff"/></svg>
      </span>
    </div>
  </header>

  <h1 class="page-title">High Tech and AdTech PR · Media Relations · Content Strategy</h1>

  <aside class="side-panel">
    <ul class="service-list">
      <li>Content Writing</li>
      <li>Inbound Marketing</li>
      <li class="is-active">Writing and Editing</li>
      <li>Positioning</li>
      <li>Workshops</li>
      <li>Public Relations</li>
    </ul>
    <div class="cta-button">Get in Touch</div>
    <svg class="phone-icon" width="16" height="16" viewBox="0 0 16 16">
      <circle cx="8" cy="8" r="8" fill="#f42a28"/>
      <path d="M5.2 4.3 L6.6 5.9 L5.9 6.8 C6.5 8 7.4 9 8.7 9.7 L9.6 9 L11.2 10.4 L10.3 11.6 C7.4 11 5.1 8.5 4.3 5.4 Z" fill="#fff"/>
    </svg>
    <div class="phone-number">555 014 2760</div>
  </aside>

  <div class="tile tile-intro">
    <p>Bluemark Communications is recognized for its ability to write and edit...</p>
    <div class="arrow-button">Learn More</div>
  </div>
  <div class="tile photo p1" role="img" aria-label="Photo of a businessman in a suit working at a desk"></div>
  <div class="tile photo p2" role="img" aria-label="Photo of a bright office window beside a computer monitor"></div>
  <div class="tile photo p3" role="img" aria-label="Photo of a suited arm resting on a desk"></div>
  <div class="tile photo p4" role="img" aria-label="Photo of a hand writing with a pen beside a keyboard"></div>
  <div class="tile photo p5" role="img" aria-label="Photo of a computer mouse and monitor base on a white desk"></div>

  <h2 class="about-heading">About Us</h2>
  <div class="small-arrow">Learn More</div>

  <article class="feature-card c1">
    <h3>Seasoned High Tech and<br>AdTech Public Relations Pros</h3>
    <p>Partner with an independent public relations resource or our team of independent communications pros.</p>
    <p>Each team member has a minimum of 15 years experience on both the agency and client side along with in-depth knowledge of the enterprise software and/or advertising technology industries.</p>
  </article>
  <article class="feature-card c2">
    <h3>Results Driven Media<br>Relations</h3>
    <p>Our strategic approach to media relations focuses on building long-term relationships with journalists and influencers. We partner with you to develop compelling business and industry stories.</p>
    <p>By taking a journalistic approach to storytelling, we work with you to uncover fresh news hooks and different angles that result in coverage.</p>
  </article>
  <article class="feature-card c3">
    <h3>Content Strategy and<br>Jargon-Free Writing</h3>
    <p>BluemarkPR excels at writing quality content. This comes from a deep understanding of technology, digital marketing, and the challenges facing CMOs and CIOs. It results in jargon-free press releases and spot on pitches that lead to conversations and coverage.</p>
  </article>

  <footer class="site-footer">
    <div class="footer-links">About Us &nbsp;|&nbsp; Contact Us &nbsp;|&nbsp; Terms &amp; Condition &nbsp;|&nbsp; Privacy Policy Copyright © 2014 Bluemark. All rights reserved</div>
  </footer>
</div>
</body>
</html>
```